Verpackungsdesign für CBD-Öl
Zielgruppe
CBD Produkte
Aufgabenstellung
Erstellung eines Designs für eine Verpackung von CBD-Öl. Die Verpackung sollte sich von den üblichen CBD Verpackungen abheben, mit Logo,, Hintergrund und Farben meiner Webseite sollte gearbeitet werden siehe Foto.
Design sollte sehr edel und cool ausschauen, nicht wie die meisten CBD Verpackungen. Eure Kreativität könnt Ihr freien Lauf lassen. Wir lassen uns überraschen.
Größe der Faltschachtel: Länge 27 mm, Breite 28 mm, Höhe 90 mm
Erstellung eines Design für eine Faltschachtel mit 4 verschiedenen Inhaltsangaben.
Das Grunddesign der Verpackung ist immer das gleiche, nur die Inhaltsangabe an Cannabidiol variiert.
10 % 1000MG, 15 % 1500MG, 20 % 2000MG, 30 % 3000MG
Kornwiese sollte im Vordergrund stehen und der Hintergrund siehe Bild!
Was draufstehen sollte
Vegan & Glutenfrei
Vollspektrum
CBD Premium Hanföl
Nicht zum Verzehr geeignet
Duftöl
Siehe Bild von Sarn, die Inhaltsstoffe bitte freihalten, da wir unterschiedliche Inhaltsstoffe/ Geschmacksrichtungen haben.
Erstellung Design für das Etikett für die 10-ml-Flasche.
Größe Etikett: Länge: 85 mm, Höhe: 30 mm
Das Grunddesign für das Label der 10-ml-Flasche ist immer das gleiche. Jedoch auch hier variiert die Inhaltsangabe von Cannabidiol.
10% 15% 20% und 30%
Auch unser Firmenlogo KORNWIESE können wir Ihnen in anderen Größen senden.
Sie können uns auch schreiben, um weitere Fragen abzuklären.
Gutes designen.

```html
<!DOCTYPE html>
<html lang="de">
<head>
<meta charset="utf-8">
<title>KORNWIESE CBD Hanföl – Faltschachtel</title>
<link rel="stylesheet" href="https://fonts.googleapis.com/css2?family=Montserrat:wght@400;600;700&family=Pathway+Gothic+One&display=swap">
<style>
  :root {
    --stage: #2a352b;
    --box-black: #1f1f1f;
    --box-dark: #171717;
    --box-grey: #2c2c2c;
    --gold: #c99a3e;
    --gold-light: #f2c24a;
    --green: #5e9a3a;
    --cream: #ece3c9;
    --white: #ffffff;
    --eu-green: #8cbf3f;
  }
  * { margin: 0; padding: 0; box-sizing: border-box; }
  html, body { width: 1200px; height: 800px; overflow: hidden; }
  body { background: var(--stage); position: relative; font-family: "Pathway Gothic One", sans-serif; }

  .dieline { position: absolute; left: 300px; top: 20px; width: 600px; height: 761px; }

  .flap-top { position: absolute; left: 300px; top: 0; width: 150px; height: 148px; background: var(--box-black); overflow: hidden; }
  .flap-bottom { position: absolute; left: 300px; top: 648px; width: 150px; height: 113px; background: #000; }
  .box-body { position: absolute; left: 0; top: 148px; width: 600px; height: 500px; background: var(--box-black); overflow: hidden; }
  .shading { position: absolute; inset: 0; }

  .brand { position: absolute; font-family: "Montserrat", sans-serif; font-weight: 600; color: var(--cream); letter-spacing: 1px; white-space: nowrap; text-align: center; }
  .flap-top .brand { left: 0; width: 150px; top: 88px; font-size: 15px; }
  .brand--front { left: 300px; width: 150px; top: 58px; font-size: 15px; }
  .brand--side { left: 8px; width: 130px; top: 246px; font-size: 15px; }

  .notice { position: absolute; left: 168px; top: 112px; font-size: 15px; line-height: 21px; color: var(--gold); }

  .usage { position: absolute; left: 165px; top: 285px; width: 125px; font-size: 10.5px; line-height: 15px; color: var(--gold); }
  .usage p { margin-bottom: 14px; }

  .leaf-art { position: absolute; border-radius: 40% 40% 10% 10%; background: linear-gradient(180deg, #b5812a, #d7b24d 60%, #6f5a2c); opacity: .85; }
  .leaf-art--side { left: 0; top: 305px; width: 68px; height: 110px; border-radius: 0 50% 40% 0; }
  .leaf-art--front { left: 318px; top: 440px; width: 112px; height: 60px; }

  .product-name { position: absolute; left: 308px; top: 118px; height: 284px; writing-mode: vertical-rl; transform: rotate(180deg); font-family: "Montserrat", sans-serif; font-size: 52px; line-height: 56px; white-space: nowrap; }
  .product-name .cbd { color: var(--green); font-weight: 700; }
  .product-name .oil { color: var(--gold); font-weight: 400; }
  .variant { position: absolute; left: 364px; top: 300px; height: 102px; writing-mode: vertical-rl; transform: rotate(180deg); font-family: "Montserrat", sans-serif; font-weight: 700; font-size: 21px; line-height: 24px; color: var(--gold); }

  .strength { position: absolute; left: 380px; top: 184px; font-family: "Montserrat", sans-serif; font-weight: 700; font-size: 29px; color: var(--gold); }
  .claim { position: absolute; left: 381px; top: 222px; font-size: 14px; line-height: 19px; color: var(--cream); }

  .features { position: absolute; left: 465px; top: 16px; list-style: none; }
  .features li { display: flex; align-items: center; gap: 8px; height: 30px; font-size: 13px; color: var(--gold); }
  .features svg { width: 26px; height: 26px; }

  .cert-badge { position: absolute; left: 466px; top: 112px; width: 74px; height: 42px; background: var(--eu-green); }

  .qualities { position: absolute; left: 466px; top: 160px; list-style: none; font-size: 10.5px; line-height: 15px; color: var(--cream); }
  .qualities li::before { content: "• "; color: var(--gold); }
  .qualities li + li { color: var(--gold); }

  .ingredients { position: absolute; left: 466px; top: 320px; font-size: 10.5px; line-height: 15px; color: var(--gold); }

  .batch { position: absolute; left: 12px; top: 12px; font-size: 15px; line-height: 22px; color: var(--white); }
  .batch-field { position: absolute; left: 8px; right: 8px; bottom: 0; height: 32px; background: var(--white); }

  .volume { position: absolute; left: 468px; top: 668px; font-size: 14px; color: var(--cream); }
</style>
</head>
<body>
<div class="dieline">

  <section class="flap-top">
    <svg class="shading" viewBox="0 0 150 148" preserveAspectRatio="none" aria-hidden="true">
      <defs>
        <linearGradient id="flapStreak" x1="0" y1="1" x2="1" y2="0">
          <stop offset="0" stop-color="#6b3d0c"/><stop offset=".5" stop-color="#f2b431"/><stop offset="1" stop-color="#5a330a"/>
        </linearGradient>
      </defs>
      <polygon points="0,138 150,108 150,118 0,148" fill="url(#flapStreak)"/>
      <polygon points="0,148 150,118 150,148" fill="#2c2c2c"/>
    </svg>
    <div class="brand">KORNWIESE</div>
  </section>

  <section class="box-body">
    <svg class="shading" viewBox="0 0 600 500" preserveAspectRatio="none" aria-hidden="true">
      <defs>
        <linearGradient id="streak" x1="0" y1="1" x2="1" y2="0">
          <stop offset="0" stop-color="#7a4a0e"/><stop offset=".3" stop-color="#ffc83a"/><stop offset=".7" stop-color="#e89a1f"/><stop offset="1" stop-color="#3a2408"/>
        </linearGradient>
      </defs>
      <polygon points="0,0 460,0 0,118" fill="var(--box-dark)"/>
      <polygon points="0,118 460,0 470,0 0,142" fill="url(#streak)"/>
      <polygon points="0,142 470,0 600,0 600,30 0,150" fill="#262626"/>
      <polygon points="0,150 600,30 600,470 0,500" fill="var(--box-grey)" opacity=".55"/>
      <polygon points="0,156 600,470 600,500 0,500" fill="#1a1a1a" opacity=".6"/>
    </svg>

    <p class="notice">Dieses Produkt ist kein<br>Arzneimittel.</p>

    <div class="brand brand--side">KORNWIESE</div>
    <div class="leaf-art leaf-art--side" role="img" aria-label="Goldenes Hanfblatt, angeschnitten"></div>

    <div class="usage">
      <p>Vor Anwendung gut schütteln. Trocken, kühl und lichtgeschützt lagern.</p>
      <p>Nicht verwenden während der Schwangerschaft und Stillzeit.</p>
      <p>Außerhalb der Reichweite von Kindern aufbewahren.</p>
      <p>Vorsicht bei Hanfallergie.</p>
      <p>Geöffnet mindestens 3 Monate haltbar.</p>
    </div>

    <div class="brand brand--front">KORNWIESE</div>
    <h1 class="product-name"><span class="cbd">CBD</span> <span class="oil">Hanföl</span></h1>
    <div class="variant">Premium</div>
    <div class="strength">10%</div>
    <p class="claim">Das volle<br>Spektrum der<br>Hanfpflanze.</p>
    <div class="leaf-art leaf-art--front" role="img" aria-label="Goldenes Hanfblatt"></div>

    <ul class="features">
      <li><svg viewBox="0 0 26 26" aria-hidden="true"><circle cx="13" cy="13" r="11" fill="none" stroke="var(--gold)" stroke-width="2"/><path d="M8 13.5l3.5 3.5 7-8" fill="none" stroke="var(--gold)" stroke-width="2"/></svg>100 % Natürlich</li>
      <li><svg viewBox="0 0 26 26" aria-hidden="true"><circle cx="13" cy="13" r="11" fill="none" stroke="var(--gold)" stroke-width="2"/><path d="M8 13.5l3.5 3.5 7-8" fill="none" stroke="var(--gold)" stroke-width="2"/></svg>100 % Vegan</li>
      <li><svg viewBox="0 0 26 26" aria-hidden="true"><circle cx="13" cy="13" r="11" fill="none" stroke="var(--gold)" stroke-width="2"/><path d="M8 13.5l3.5 3.5 7-8" fill="none" stroke="var(--gold)" stroke-width="2"/></svg>100 % Glutenfrei</li>
    </ul>
    <div class="cert-badge" role="img" aria-label="Bio-Siegel"></div>
    <ul class="qualities">
      <li>Biozertifiziert</li>
      <li>Voller Terpeneffekt</li>
      <li>Keine Konservierungsstoffe</li>
    </ul>
    <p class="ingredients">Inhaltsstoffe:<br>Bio Hanfsamenöl<br>(kaltgepresst)<br>Bio Hanfsamenextrakt</p>
  </section>

  <section class="flap-bottom">
    <p class="batch">Charge:<br>Mindestens haltbar bis:</p>
    <div class="batch-field"></div>
  </section>

  <div class="volume">10 ml</div>
</div>
</body>
</html>
```